Wordpress Web Design & Coding for velqorahealth.ca

We need a website for a new investment company that is visually grabbing and vibrant. We would like to see a web page that displays trust, growth and confidence. Needs to be responsive and mobile friendly for all browsers and coded for both Android & IOS.

Open to the number of pages and menu items. I selected 4 but if you feel the layout would work better with less I am open to this. Need to sell the people (management team/related businesses) and then show where the invested money will be going (upcoming projects).

Company Info:

Velq Ora is an investment company put together by a group of seasoned business professionals who have come together to combine decades of success in the real estate development, management, financing and medical services. The company will be a full service company offering turn key solutions for medical professionals.

Velq-Ora will focus on providing a full range of services via a group of distinct companies to deliver newly emerging needs of the medical community. The end goal will be to create complete solutions for individuals in the medical community. Our group has experience and success with the conceptualization, construction and financing of medical and dental clinic spaces. Velq-Ora Solutions will be established to accommodate all areas of the development and creation of clinics for medical professionals from building construction to equipment financing and administrations.

You can mention these companies and take photos from their websites. You can also use stock photos.

Our construction partner:
https://812bld.com/projects/

Our equipment leasing partner:
https://www.lomerix.com/

Our Management Team and medical partners

Dale Pickett
https://www.yourcalmpath.ca/

Milos Vandergrift
https://www.qhzdentalservices.com/about-us

PROPOSED PROJECTS (see attachment for details)
Harlow Ridge Business Park
Dunmere Business Park
Mt. Corwin Way Professional

Target Market(s)

Investors

Industry/Entity Type

Investment

Coding

Coded - Design and coding required

Number of Pages Required

4 page

Font styles to use
Sans Serif

Requirements
Must have
• Wordpress – must be both desktop and mobile friendly with fast page load speed
Ability to edit after ourselves in Wordpress
Attractive home page with logo etc.
Logo colours are: for the blue the pantone color is #0355a3
and for the green is #8cc63f

Sections, about us, what we do/services we provide, contact us

```html
<!DOCTYPE html>
<html lang="en">
<head>
<meta charset="utf-8">
<title>Velq-Ora Solutions — Home</title>
<link rel="stylesheet" href="https://fonts.googleapis.com/css2?family=Barlow:wght@500;600;700&family=Lato:wght@400;700&display=swap">
<style>
  :root {
    --brand-blue: #0355a3;
    --brand-blue-light: #1a67b3;
    --brand-green: #8cc63f;
    --brand-green-light: #9bd04f;
    --ink: #2a2a2a;
    --muted: #666;
    --hero-bg: #f2f2f2;
    --white: #ffffff;
    --divider: rgba(255,255,255,.18);
  }
  * { margin: 0; padding: 0; box-sizing: border-box; }
  html, body { width: 1200px; height: 775px; overflow: hidden; background: var(--white); }
  body { font-family: "Lato", sans-serif; color: var(--ink); position: relative; }

  .site-header {
    position: absolute; left: 0; top: 0; width: 1200px; height: 107px;
    background: linear-gradient(105deg, var(--brand-blue) 0 48%, var(--brand-blue-light) 48% 60%, var(--brand-blue) 60% 100%);
  }
  .brand { position: absolute; left: 235px; top: 16px; display: flex; align-items: center; gap: 9px; }
  .brand-mark { width: 26px; height: 26px; background: var(--brand-green); }
  .brand-name { font-family: "Barlow", sans-serif; font-weight: 700; font-size: 26px; color: var(--white); letter-spacing: .5px; }

  .contact-bar {
    position: absolute; left: 600px; top: 0; height: 70px;
    display: flex; border-left: 1px solid var(--divider);
  }
  .contact-info {
    display: flex; align-items: center; gap: 11px; height: 70px;
    padding: 0 28px 0 30px; border-right: 1px solid var(--divider);
  }
  .contact-info.phone { padding-left: 26px; }
  .contact-text { font-size: 9.5px; line-height: 15px; color: var(--white); white-space: nowrap; }
  .contact-text strong { font-weight: 700; }

  .main-nav { position: absolute; left: 235px; top: 79px; display: flex; }
  .main-nav a { font-size: 9.5px; color: var(--white); text-decoration: none; text-transform: uppercase; margin-right: 26px; }
  .main-nav a.current { color: var(--brand-green); margin-right: 46px; }
  .social-row { position: absolute; left: 890px; top: 80px; display: flex; gap: 11px; }
  .social-row span { width: 8px; height: 8px; border-radius: 50%; background: var(--brand-green); opacity: .85; }

  .hero { position: absolute; left: 0; top: 107px; width: 1200px; height: 343px; background: var(--hero-bg); overflow: hidden; }
  .hero-photo {
    position: absolute; left: 680px; top: 0; width: 380px; height: 343px;
    background: linear-gradient(90deg, rgba(242,242,242,1) 0%, #c9c9c9 35%, #8a8a8a 60%, #b5b5b5 85%, rgba(242,242,242,1) 100%);
  }
  .hero-title { position: absolute; left: 235px; top: 46px; width: 480px; font-family: "Barlow", sans-serif; font-weight: 700; font-size: 31px; line-height: 38px; color: var(--ink); }
  .hero-lead { position: absolute; left: 235px; top: 172px; width: 360px; font-size: 11px; line-height: 18px; color: var(--muted); }
  .btn-solid { position: absolute; left: 235px; top: 234px; width: 106px; height: 28px; background: var(--brand-green); color: var(--ink); font-size: 8.5px; text-transform: uppercase; display: flex; align-items: center; justify-content: center; gap: 4px; }
  .slider-dots { position: absolute; left: 564px; top: 315px; display: flex; gap: 6px; }
  .slider-dots span { width: 20px; height: 3px; background: #cfcfcf; }
  .slider-dots span.active { background: var(--brand-green); }

  .cta-band {
    position: absolute; left: 0; top: 450px; width: 1200px; height: 75px;
    background: linear-gradient(105deg, var(--brand-green) 0 58%, var(--brand-green-light) 58% 68%, var(--brand-green) 68% 100%);
  }
  .cta-text { position: absolute; left: 235px; top: 29px; font-size: 12px; color: #2f4a10; text-transform: uppercase; letter-spacing: .2px; }
  .btn-outline { position: absolute; left: 880px; top: 24px; width: 85px; height: 27px; border: 1.5px solid #2f4a10; color: #2f4a10; font-size: 8px; text-transform: uppercase; display: flex; align-items: center; justify-content: center; }

  .about { position: absolute; left: 0; top: 525px; width: 1200px; height: 250px; background: var(--white); }
  .about-photo { position: absolute; left: 235px; top: 84px; width: 232px; height: 166px; background: linear-gradient(135deg, #6b5a52, #a8897a 55%, #4a3f3a); }
  .about-copy { position: absolute; left: 487px; top: 90px; width: 470px; }
  .eyebrow { font-family: "Barlow", sans-serif; font-weight: 600; font-size: 14px; color: var(--ink); display: flex; align-items: center; gap: 8px; }
  .eyebrow::after { content: ""; width: 24px; height: 2px; background: var(--brand-green); }
  .about-title { font-family: "Barlow", sans-serif; font-weight: 700; font-size: 21px; color: var(--ink); margin-top: 8px; text-transform: uppercase; letter-spacing: .3px; }
  .about-text { font-size: 11px; line-height: 18px; color: var(--muted); margin-top: 14px; }
</style>
</head>
<body>
  <header class="site-header">
    <div class="brand">
      <span class="brand-mark"></span>
      <span class="brand-name">Velq-Ora</span>
    </div>

    <div class="contact-bar">
      <div class="contact-info address">
        <svg width="16" height="20" viewBox="0 0 16 20" fill="none" stroke="#fff" stroke-width="1.4"><path d="M8 19s6-6.4 6-11A6 6 0 0 0 2 8c0 4.6 6 11 6 11z"/><circle cx="8" cy="8" r="2.2"/></svg>
        <div class="contact-text"><strong>58 CALDER ROW,</strong><br>Brookmere, NY 11482</div>
      </div>
      <div class="contact-info phone">
        <svg width="14" height="20" viewBox="0 0 14 20" fill="none" stroke="#fff" stroke-width="1.4"><rect x="2" y="1" width="10" height="18" rx="2"/><line x1="5.5" y1="16" x2="8.5" y2="16"/></svg>
        <div class="contact-text"><strong>(555)-014-2276</strong><br>contact@velqorahealth.ca</div>
      </div>
    </div>

    <nav class="main-nav">
      <a class="current" href="#">Home</a>
      <a href="#">About Us</a>
      <a href="#">What We Do</a>
      <a href="#">Contact Us</a>
    </nav>

    <div class="social-row" aria-label="Social links"><span></span><span></span><span></span><span></span></div>
  </header>

  <section class="hero">
    <div class="hero-photo" role="img" aria-label="Black and white photo of a doctor and a nurse reviewing a tablet in a bright modern hospital corridor"></div>
    <h1 class="hero-title">One of our strategic goals is to assist the medical community in catering to those services.</h1>
    <p class="hero-lead">We are a group of seasoned business professionals who have come to-gether to combine decades of success in the real estate development.</p>
    <a class="btn-solid">View Services
      <svg width="9" height="6" viewBox="0 0 9 6" fill="none" stroke="#2a2a2a" stroke-width="1"><path d="M0 3h8M6 1l2 2-2 2"/></svg>
    </a>
    <div class="slider-dots"><span class="active"></span><span></span><span></span></div>
  </section>

  <section class="cta-band">
    <p class="cta-text">Are you looking to setup a hospital? We can help!</p>
    <a class="btn-outline">Contact Us</a>
  </section>

  <section class="about">
    <div class="about-photo" role="img" aria-label="Portrait photo of a smiling team member in glasses"></div>
    <div class="about-copy">
      <p class="eyebrow">Who We Are</p>
      <h2 class="about-title">Having 25 Years Experience</h2>
      <p class="about-text">We bring together partners in construction, leasing, financing and clinic administration so medical professionals can open new practices with confidence.</p>
    </div>
  </section>
</body>
</html>
```